Wordpress - For IT, Cloud/Hosting, Residential/Commercial Construction Services

We are a holding company for service companies. We want the current Wordpress site modified or a new wordpress site completed. We want this site to be the parent website, that then has pull down menus linking to our other website (currently http://tallowbrook.example, http://q4q.example and would like it to be easy and fluid as we acquire more companies as we have with KTVN, Inc., J&J Construction, Tallow Brook etc. Model after sites like Vexlo.example, Quandrix.example, ZLT.example,.farrowgate.example

------

The parent is the main site q4q Corp. Below that are sub corps and DBAs. q4q Corp stands for Quiet 4 Quest Corp. q4q Offers IT manages services, 24x7 support, Monitoring NOC, Remote Hands, Onsite support services. We have acquired KTVN, Inc, J & J Construction, TallowBrook.example. We plan to acquire/spin up many companies that offer service, support and installation offerings and will all be known as an q4q Corp Company for branding purposes. We recently had our logo done, but then ran it through 3d glass as we like the look better than the original works. We have original files in vector, but not the 3D galss door render.

Target Market(s)

IT Server and Desktop Support. Construction. Mold Remediation. Mergers and Acquisitions.

Industry/Entity Type

It Company

Coding

Coded - Design and coding required

Font styles to use
Sans Serif

Colors
0792cd

Requirements
Must have
• Clean interface. Modern design. Mobile device and multi browser support. Must be for Wordpress. Job posting with resume submission module.Hook to our Web hosting portal (Plesk) API into BriteNQ Reseller portal, customer portal to allow payments to their account etc.. Easy to edit. Easy to add to, Press Release Section, Investor Relations etc.
Should not have
• Slow loading. Played out design. Over use of stock images. Copied from a competitor or something point to such.

```html
<!DOCTYPE html>
<html lang="en">
<head>
<meta charset="utf-8">
<title>q4q Corp</title>
<link href="https://fonts.googleapis.com/css2?family=Open+Sans:ital,wght@0,400;0,600;0,700;0,800;1,400&display=swap" rel="stylesheet">
<style>
:root{
  --brand:#0f76c0;
  --brand-dark:#0b5f9e;
  --hero-a:#1d5f8f;
  --hero-b:#2f86b8;
  --strip:#e2f1fb;
  --ink:#333;
  --muted:#666;
  --grey-band:#ebebeb;
  --footer:#141414;
  --footer-line:#2c2c2c;
  --white:#fff;
}
*{margin:0;padding:0;box-sizing:border-box}
html,body{width:1200px;height:3046px;overflow:hidden}
body{font-family:'Open Sans',Arial,sans-serif;color:var(--ink);background:var(--white);position:relative}
a{color:inherit;text-decoration:none}

/* hero */
.hero{position:absolute;left:0;top:0;width:1200px;height:780px;
  background:linear-gradient(160deg,#3a86b4 0%,var(--hero-b) 35%,var(--hero-a) 100%);color:var(--white)}
.hero-photo{position:absolute;inset:0;background:radial-gradient(ellipse at 45% 35%,rgba(160,205,230,.35),transparent 60%)}
.topbar{position:absolute;top:24px;right:108px;display:flex;gap:24px;font-size:12px;font-weight:600}
.topbar span{display:flex;align-items:center;gap:5px}
.logo{position:absolute;left:112px;top:70px;display:flex;align-items:center;gap:10px;font-size:24px;font-weight:700;line-height:1;color:var(--white)}
.logo .square{width:22px;height:22px;background:var(--white);display:block}
.main-nav{position:absolute;top:78px;left:430px;display:flex;font-size:15px;font-weight:600}
.main-nav a{display:block;padding:0 19px;line-height:22px}
.main-nav .active{border-bottom:2px solid #fff;padding-bottom:8px}
.main-nav .nav-solutions{margin-left:16px}
.dropdown{position:absolute;left:747px;top:116px;width:230px;border:1px solid rgba(255,255,255,.8);background:rgba(20,80,120,.25);font-size:15px}
.dropdown div{height:41px;line-height:41px;padding-left:28px;border-bottom:1px solid rgba(255,255,255,.8)}
.dropdown div:last-child{border-bottom:0}
.hero-title{position:absolute;top:330px;left:0;width:1200px;text-align:center;font-size:74px;font-weight:800;letter-spacing:1px}
.hero-sub{position:absolute;top:424px;left:0;width:1200px;text-align:center;font-size:17px;font-weight:600;line-height:26px}
.scroll-mouse{position:absolute;left:584px;top:672px}

/* brand strip */
.brand-strip{position:absolute;top:780px;left:0;width:1200px;height:75px;background:var(--strip);display:flex;align-items:center;justify-content:center;gap:34px;font-weight:700;font-size:16px;color:#222}

/* services */
.section-title{font-size:33px;font-weight:800;color:#2b2b2b;text-align:center}
.services .section-title{position:absolute;top:922px;left:0;width:1200px}
.services .lead{position:absolute;top:988px;width:1200px;text-align:center;font-size:14px;color:var(--muted)}
.service{position:absolute;top:1083px;width:240px;text-align:center}
.service .ring{width:152px;height:152px;border:3px solid var(--brand);border-radius:50%;margin:0 auto;display:flex;align-items:center;justify-content:center}
.service h3{margin-top:30px;font-size:20px;font-weight:600;color:var(--brand)}
.btn{display:inline-flex;align-items:center;justify-content:center;gap:10px;background:var(--brand);color:#fff;font-weight:700;font-size:14px;border-radius:26px;text-transform:uppercase}
.btn-services{position:absolute;left:471px;top:1384px;width:258px;height:51px}

/* about */
.about{position:absolute;top:1525px;left:0;width:1200px;height:522px;background:var(--grey-band)}
.about h2{position:absolute;left:112px;top:62px;font-size:33px;font-weight:800;color:#2b2b2b}
.about .copy{position:absolute;left:112px;top:122px;width:486px;font-size:13.5px;line-height:23px;color:#444}
.about .copy p{margin-bottom:12px}
.about .copy p.tight{margin-bottom:0}
.btn-more{position:absolute;left:112px;top:396px;width:199px;height:44px}
.about-photo{position:absolute;left:605px;top:73px;width:483px;height:367px;background:#a9cde0;padding:12px}
.about-photo div{width:100%;height:100%;background:linear-gradient(135deg,#d7d2c8,#8f8c86 55%,#5a5d62)}

/* testimonials */
.testimonials{position:absolute;top:2047px;left:0;width:1200px;height:544px;background:linear-gradient(180deg,#1a6cad,#1660a0);color:#fff}
.testimonials .section-title{position:absolute;top:70px;left:0;width:1200px;color:#fff}
.quote-card{position:absolute;top:186px;height:189px;background:#fff;color:#555;text-align:center;padding:14px 22px}
.quote-card::after{content:"";position:absolute;left:50%;bottom:-14px;margin-left:-14px;border:14px solid transparent;border-bottom:0;border-top-color:#fff}
.quote-mark{font-size:54px;font-weight:800;color:var(--brand);line-height:54px;height:46px}
.quote-card p{font-size:12.5px;font-style:italic;line-height:23px}
.author{position:absolute;top:398px;display:flex;align-items:center;gap:10px}
.avatar{width:44px;height:44px;border-radius:50%;background:linear-gradient(135deg,#c9a58a,#6f5647);border:2px solid #fff}
.author b{display:block;font-size:17px;font-weight:700}
.author small{font-size:12px}

/* footer */
.site-footer{position:absolute;top:2591px;left:0;width:1200px;height:455px;background:var(--footer);color:#ddd}
.site-footer h4{font-size:16px;font-weight:700;color:#fff;text-transform:uppercase;position:absolute;top:80px}
.f-col{position:absolute;top:126px;font-size:13px}
.contact-row{display:flex;gap:16px;align-items:flex-start;line-height:21px;margin-bottom:20px;width:220px}
.links li{list-style:none;margin-bottom:16px;display:flex;gap:14px;align-items:center}
.links li::before{content:"»";font-size:13px}
.email-field{width:284px;height:40px;border-radius:20px;background:#fff;color:#777;font-size:13px;padding:0 24px;line-height:40px;margin-top:26px}
.btn-sub{width:122px;height:40px;margin-top:14px;font-size:13px}
.footer-bottom{position:absolute;left:112px;top:368px;width:976px;border-top:1px solid var(--footer-line)}
.copyright{position:absolute;left:112px;top:398px;font-size:12px}
.socials{position:absolute;left:972px;top:391px;display:flex;gap:8px}
.socials span{width:32px;height:32px;border:1px solid #bbb;border-radius:50%;display:flex;align-items:center;justify-content:center;font-size:10px;font-weight:600;color:#ddd}
</style>
</head>
<body>

<header class="hero">
  <div class="hero-photo" role="img" aria-label="Blue-tinted photo of two business people shaking hands over a desk"></div>
  <div class="topbar">
    <span>✎ LOGIN</span><span>▪ CAREERS</span><span>✆ CONTACT US</span>
    <span><svg width="12" height="12" viewBox="0 0 12 12"><circle cx="5" cy="5" r="3.6" fill="none" stroke="#fff" stroke-width="1.8"/><path d="M8 8l3 3" stroke="#fff" stroke-width="1.8"/></svg></span>
  </div>
  <div class="logo"><span class="square"></span><span>q4q Corp</span></div>
  <nav class="main-nav">
    <a class="active">HOME</a><a>ABOUT US</a><a>OUR SERVICES</a><a>COMPANIES ⌄</a><a class="nav-solutions">SOLUTIONS</a><a>BLOG</a>
  </nav>
  <div class="dropdown">
    <div>KTVN Inc</div><div>J&amp;J Construction</div><div>Tallow Brook</div><div>q4q host</div>
  </div>
  <h1 class="hero-title">Q4Q CORP</h1>
  <p class="hero-sub">Utenim inima veniam quis nostrum exercitationem<br>ullam corporis susboriosam</p>
  <svg class="scroll-mouse" width="32" height="50" viewBox="0 0 32 50"><rect x="2" y="2" width="28" height="46" rx="14" fill="none" stroke="#fff" stroke-width="2.5"/><path d="M16 11v8" stroke="#fff" stroke-width="2.5"/><path d="M10 30l6 6 6-6" fill="none" stroke="#fff" stroke-width="2.5"/></svg>
</header>

<section class="brand-strip">
  <span>Tunora</span><span>Parcelo Plus</span><span>vimba</span><span>REELIO</span><span>KORVAN</span><span>Ultra Vista</span><span>Peakline</span><span>MX</span><span>NRB</span><span>Solmara</span>
</section>

<section class="services">
  <h2 class="section-title">OUR SERVICES</h2>
  <p class="lead">Sed ut perspiciatis unde omnis iste natus error sit voluptatem accusantium doloremque laudantium,</p>

  <div class="service" style="left:81px">
    <div class="ring"><svg width="70" height="60" viewBox="0 0 70 60" fill="none" stroke="#0f76c0" stroke-width="2.5"><rect x="4" y="4" width="62" height="40" rx="2"/><path d="M28 44v8M42 44v8M20 54h30"/><circle cx="35" cy="24" r="7"/><circle cx="35" cy="24" r="12" stroke-dasharray="4 3"/></svg></div>
    <h3>IT Services</h3>
  </div>
  <div class="service" style="left:339px">
    <div class="ring"><svg width="76" height="60" viewBox="0 0 76 60" fill="none" stroke="#0f76c0" stroke-width="2.5"><path d="M18 44a12 12 0 0 1 0-24 16 16 0 0 1 30-4 12 12 0 0 1 16 14"/><rect x="30" y="28" width="40" height="26" rx="3"/><path d="M30 36h40M36 46h10"/></svg></div>
    <h3>Cloud/Hosting</h3>
  </div>
  <div class="service" style="left:595px">
    <div class="ring"><svg width="80" height="60" viewBox="0 0 80 60" fill="none" stroke="#0f76c0" stroke-width="2.5"><path d="M6 28L24 12l18 16M38 24l18-16 18 16M10 26v28h60V26"/><rect x="18" y="34" width="8" height="8"/><rect x="52" y="34" width="8" height="8"/><rect x="35" y="38" width="10" height="16"/></svg></div>
    <h3>Home/Commercial</h3>
  </div>
  <div class="service" style="left:852px">
    <div class="ring"><svg width="66" height="62" viewBox="0 0 66 62" fill="none" stroke="#0f76c0" stroke-width="2.5"><rect x="4" y="6" width="46" height="52"/><path d="M50 10h8a4 4 0 0 1 4 4v44H50"/><path d="M12 18h16v12h12M12 40h10v10M30 40h12"/></svg></div>
    <h3>Construction Services</h3>
  </div>

  <a class="btn btn-services">View all services <svg width="14" height="14" viewBox="0 0 14 14"><circle cx="7" cy="7" r="7" fill="#fff"/><path d="M5 4l3 3-3 3" stroke="#0f76c0" stroke-width="2" fill="none"/></svg></a>
</section>

<section class="about">
  <h2>ABOUT Q4Q CORP</h2>
  <div class="copy">
    <p>q4q Corp is a Netrowe and Quandrix IT Solution Provider. We provide support for Desktops, Laptops, Tablets, Mobile Devices, Networking, WiFi, Server, Design and more by providing Remote and OnSite Support Services.</p>
    <p class="tight">q4q Corp (Quiet 4 Quest) Full service one stop shop service provider. Our CEO and Founder Dale Korvin has been working with Quandrix Solutions all the way back to QX Dos and all the way to Quandrix's full solution offerings of today. He trains his team to be clones of his highly technical mindset of "can do it all aptitude" because he feels nothing in technology is cut and dry, as each client and each technology work uniquely!</p>
    <p>q4q is a Netrowe and Quandrix IT Solution partner.</p>
  </div>
  <a class="btn btn-more">Learn more</a>
  <div class="about-photo"><div role="img" aria-label="Photo of business people talking in a bright glass office lobby"></div></div>
</section>

<section class="testimonials">
  <h2 class="section-title">WHAT OUR CLIENTS SAY</h2>

  <div class="quote-card" style="left:112px;width:316px"><div class="quote-mark">“</div><p>In ullamcorper est eget tempor cursus neque mi consectetuer mi a ultricies massa est sed nisl Class aptent taciti sociosqu ad litora torquent per conubia nostra</p></div>
  <div class="quote-card" style="left:445px;width:318px"><div class="quote-mark">“</div><p>In ullamcorper est eget tempor cursus neque mi consectetuer mi a ultricies massa est sed nisl Class aptent taciti sociosqu ad litora torquent per conubia nostra</p></div>
  <div class="quote-card" style="left:778px;width:310px"><div class="quote-mark">“</div><p>In ullamcorper est eget tempor cursus neque mi consectetuer mi a ultricies massa est sed nisl Class aptent taciti sociosqu ad litora torquent per conubia nostra</p></div>

  <div class="author" style="left:182px"><div class="avatar" role="img" aria-label="Client portrait"></div><div><b>By Author</b><small>City, Location</small></div></div>
  <div class="author" style="left:516px"><div class="avatar" role="img" aria-label="Client portrait"></div><div><b>By Author</b><small>City, Location</small></div></div>
  <div class="author" style="left:862px"><div class="avatar" role="img" aria-label="Client portrait"></div><div><b>By Author</b><small>City, Location</small></div></div>
</section>

<footer class="site-footer">
  <h4 style="left:112px">Contact us</h4>
  <h4 style="left:378px">Quick links</h4>
  <h4 style="left:587px">Other links</h4>
  <h4 style="left:804px">Stay connected</h4>

  <div class="f-col" style="left:112px">
    <div class="contact-row"><svg width="18" height="22" viewBox="0 0 18 22" fill="none" stroke="#ddd" stroke-width="1.6"><path d="M9 21s7-7.5 7-12A7 7 0 0 0 2 9c0 4.5 7 12 7 12z"/><circle cx="9" cy="9" r="2.5"/></svg><span>12,Sed ut perspiciatis un om iste natus error...,</span></div>
    <div class="contact-row"><svg width="18" height="18" viewBox="0 0 18 18" fill="none" stroke="#ddd" stroke-width="1.6"><path d="M4 1l3 4-2 2a10 10 0 0 0 6 6l2-2 4 3-2 3C8 17 1 10 1 3z"/></svg><span>Phone : 1 800 555 0142</span></div>
    <div class="contact-row"><svg width="18" height="14" viewBox="0 0 18 14" fill="none" stroke="#ddd" stroke-width="1.6"><rect x="1" y="1" width="16" height="12"/><path d="M1 1l8 7 8-7"/></svg><span>info@q4qcorp.example</span></div>
  </div>

  <ul class="f-col links" style="left:380px"><li>Home</li><li>About us</li><li>Services</li><li>Companies</li><li>Contact us</li></ul>
  <ul class="f-col links" style="left:589px"><li>My Account</li><li>Sitemap</li><li>Terms of service</li><li>Blog</li><li>Login</li></ul>

  <div class="f-col" style="left:804px">
    <p>Sed ut perspiciatis unde omnis iste...</p>
    <div class="email-field">Enter Email</div>
    <a class="btn btn-sub">Subscribe</a>
  </div>

  <div class="footer-bottom"></div>
  <p class="copyright">© copyright 2018 &nbsp;q4q Corp. All Rights Reserved &nbsp;| &nbsp;Privacy policy</p>
  <div class="socials" aria-label="Social links"><span>Zo</span><span>Kip</span><span>Vu</span></div>
</footer>

</body>
</html>
```